RAIL RIGHT FITTERS

We deliver and install grab bars aka grab rails, bath rails, safety rails. same day delivery and installation on almost ANY surface.
not covered by health insurance. most people cannot find anyone to install grab bars. we offer standard grab bars including delivery and installation for $89.95. standard includes choice of white, chrome or pewter 16 inch bars. if 2 bars are installed $84.95 each and 3 for $79.95 each.we also offer designer bars as well as angle configurations.

grab bars can be installed in any room, bathroom, bedroom, kitchen, stairway, garage, workshop, front and backdoor, bathtub, shower stall, toilet area , laundry room and just about any other place you can think of. not only elderly-everyone can benefit                                

Industry/Entity Type

Safety

Requirements
Must have
• eliminate any correlation to brightpath in house website. this flyer should be its own for rail right fitters inc.
Nice to have
• maybe sketch or cartoon in nature ie moving van(delivery)
grab bar attached to van ( product)
character holding on to bar with wrench in other hand (installation)
pricing bursts or clouds enphasizing special $$$

```html
<!DOCTYPE html>
<html lang="en">
<head>
<meta charset="utf-8">
<title>Rail Right Fitters – Flyer</title>
<link rel="stylesheet" href="https://fonts.googleapis.com/css2?family=Cabin:wght@400;600;700&family=Cabin+Condensed:wght@600;700&family=Kaushan+Script&family=Caveat:wght@600&display=swap">
<style>
  :root {
    --green-deep: #0f4d2a;
    --green-mid: #1d6b36;
    --green-bright: #3f9a3c;
    --green-lime: #8cc63f;
    --yellow: #f3e23a;
    --white: #ffffff;
    --ink: #1f2a22;
    --scene-top: #e9eee8;
    --scene-bottom: #c9d6cb;
  }
  * { box-sizing: border-box; margin: 0; padding: 0; }
  html, body { width: 900px; height: 1200px; overflow: hidden; background: #fff; }
  body { font-family: "Cabin", sans-serif; color: var(--white); }

  .flyer { position: relative; width: 900px; height: 1200px; overflow: hidden; background: var(--green-deep); }

  .hero-scene {
    position: absolute; left: 0; top: 0; width: 900px; height: 620px;
    background: linear-gradient(160deg, var(--scene-top) 0%, #dfe6de 45%, var(--scene-bottom) 100%);
  }
  .hero-illustration {
    position: absolute; left: 230px; top: 235px; width: 370px; height: 320px;
    border-radius: 18px;
    background: radial-gradient(ellipse at 50% 45%, #f2d3b4 0%, #d94b3b 45%, #5b8fc9 80%, rgba(91,143,201,0) 100%);
    opacity: .55;
  }
  .speech-bubble {
    position: absolute; left: 640px; top: 290px; width: 160px; height: 96px;
    background: var(--white); border: 2px solid var(--ink); border-radius: 50%;
    display: flex; align-items: center; justify-content: center; text-align: center;
    font-family: "Caveat", cursive; font-size: 22px; line-height: 1.05; color: var(--ink);
    padding: 10px 18px;
  }

  .price-badge {
    position: absolute; left: 0; top: 0; width: 300px; height: 215px;
    background: var(--green-deep); text-align: center; padding-top: 20px;
  }
  .price-badge .only { font-family: "Cabin Condensed", sans-serif; font-size: 32px; color: var(--yellow); letter-spacing: 1px; }
  .price-badge .amount { font-family: "Cabin Condensed", sans-serif; font-weight: 700; font-size: 78px; line-height: .95; color: var(--yellow); }
  .price-badge .note { font-size: 20px; margin-top: 8px; line-height: 1.2; }

  .brand-name {
    position: absolute; left: 360px; top: 60px; width: 520px; text-align: center;
    font-family: "Cabin Condensed", sans-serif; font-weight: 700; font-size: 72px; line-height: .95;
    color: var(--green-mid); letter-spacing: 2px; text-transform: uppercase;
  }

  .wave-band { position: absolute; left: 0; top: 540px; width: 900px; height: 90px; }

  .offer-column { position: absolute; left: 0; top: 640px; width: 400px; padding: 0 34px; text-align: center; }
  .offer-title { font-family: "Kaushan Script", cursive; color: var(--yellow); font-size: 44px; line-height: 1; }
  .offer-title small { display: block; font-size: 28px; color: var(--white); margin-left: 110px; }
  .deal-list { list-style: none; margin: 18px 0 0; }
  .deal-list li {
    background: var(--green-mid); border: 2px solid var(--green-lime); margin-bottom: 10px;
    padding: 6px 12px; font-size: 20px; text-align: left;
  }
  .deal-list strong { font-family: "Cabin Condensed", sans-serif; font-size: 28px; color: var(--yellow); }
  .same-day { margin-top: 12px; font-family: "Cabin Condensed", sans-serif; font-weight: 700; font-size: 30px; color: var(--yellow); line-height: 1.05; }
  .same-day span { display: block; font-family: "Cabin", sans-serif; font-weight: 400; font-size: 20px; color: var(--white); margin-top: 6px; }

  .column-rule { position: absolute; left: 412px; top: 660px; width: 2px; height: 250px; background: var(--green-lime); }

  .rooms-column { position: absolute; left: 440px; top: 650px; width: 430px; }
  .rooms-title { font-family: "Cabin Condensed", sans-serif; font-weight: 700; font-size: 32px; color: var(--yellow); line-height: 1; }
  .rooms-sub { font-weight: 700; font-size: 16px; color: var(--green-lime); letter-spacing: .5px; margin-top: 4px; }
  .rooms-body { display: flex; gap: 20px; margin-top: 12px; }
  .room-list { list-style: none; font-size: 16px; line-height: 1.3; width: 190px; }
  .room-list li::before { content: "• "; color: var(--green-lime); }
  .rooms-extra { font-size: 16px; line-height: 1.3; width: 220px; }
  .product-illustration {
    margin-top: 16px; width: 210px; height: 58px; border-radius: 8px;
    background: linear-gradient(90deg, #9aa6a0, #e6ebe8 50%, #9aa6a0);
    opacity: .8;
  }

  .contact-band {
    position: absolute; left: 0; top: 1030px; width: 900px; height: 170px;
    background: var(--green-bright); padding: 24px 34px;
  }
  .call-label { font-size: 26px; font-weight: 700; color: var(--green-deep); letter-spacing: 1px; }
  .phone { font-family: "Cabin Condensed", sans-serif; font-weight: 700; font-size: 70px; line-height: 1; color: var(--white); }
  .caller-silhouette {
    position: absolute; left: 560px; top: 38px; width: 70px; height: 90px; border-radius: 40px 40px 10px 10px;
    background: linear-gradient(180deg, var(--green-deep), #2b5a35); opacity: .85;
  }
  .tagline {
    position: absolute; left: 645px; top: 38px; width: 230px;
    font-family: "Caveat", cursive; font-size: 40px; line-height: 1; color: var(--white);
  }
</style>
</head>
<body>
<main class="flyer">
  <div class="hero-scene" role="img" aria-label="Cartoon background: a white door with a grab bar mounted beside it">
    <div class="hero-illustration" role="img" aria-label="Cartoon installer character holding a grab bar"></div>
  </div>
  <div class="speech-bubble">I can make your home safer!</div>

  <section class="price-badge">
    <p class="only">ONLY</p>
    <p class="amount">$89.95</p>
    <p class="note">( includes bar &amp;<br>installation )</p>
  </section>

  <h1 class="brand-name">Rail Right<br>Fitters</h1>

  <svg class="wave-band" viewBox="0 0 900 90" preserveAspectRatio="none" aria-hidden="true">
    <path d="M0 50 Q450 -20 900 30 L900 90 L0 90 Z" fill="#3f9a3c"/>
    <path d="M0 80 Q450 15 900 65 L900 90 L0 90 Z" fill="#0f4d2a"/>
  </svg>

  <section class="offer-column">
    <h2 class="offer-title">We deliver<small>and install</small></h2>
    <ul class="deal-list">
      <li>Buy 2 for only <strong>$84.95</strong></li>
      <li>Buy 3 for only <strong>$79.95</strong></li>
    </ul>
    <p class="same-day">Same day delivery &amp;<br>installation!!<span>on almost ANY surface.</span></p>
  </section>

  <div class="column-rule"></div>

  <section class="rooms-column">
    <h2 class="rooms-title">GRAB BARS</h2>
    <p class="rooms-sub">CAN BE INSTALLED IN ANY ROOM!</p>
    <div class="rooms-body">
      <ul class="room-list">
        <li>Bathroom</li><li>Bedroom</li><li>Kitchen</li><li>Stairway</li><li>Garage</li>
        <li>Workshop</li><li>Front and backdoor</li><li>Bathtub</li><li>Shower stall</li>
        <li>Toilet area</li><li>Laundry room</li>
      </ul>
      <div>
        <p class="rooms-extra">and just about any other place you can think of. not only elderly-everyone can benefit.</p>
        <div class="product-illustration" role="img" aria-label="Two chrome grab bars"></div>
      </div>
    </div>
  </section>

  <footer class="contact-band">
    <p class="call-label">CALL US NOW:</p>
    <p class="phone">1-800-555 0147</p>
    <div class="caller-silhouette" role="img" aria-label="Silhouette of a person on the phone"></div>
    <p class="tagline">"One call is all it takes"</p>
  </footer>
</main>
</body>
</html>
```